1912 Zur Glutpfanne Website
Zielgruppe
Wir betreiben ein Hamburger-Restaurant. Alle Zutaten kommen wenn möglich, aus der Region. Wir benutzen keine Farb- und Konservierungsstoffe. Unser Fleisch ist ein frisches Bio-Rinderhack. Das Brot backen wir selber und die Saucen sind nach eigener Rezeptur hausgemacht. Der Käse wird in einem Familienbetrieb frisch für uns hergestellt. Jeder Gast kann sich seinen Burger frisch nach seinen Wünschen zusammenstellen und bei der Zubereitung zuschauen. Essen mit Herkunft aus Tradition!
Aufgabenstellung
Ansprechendes Design, welches unsere Philosophie und die Liebe zum Burger widerspiegelt. Frische Zutaten in wechselnden Slide-Shows, Wertschätzung der Rohprodukte und den Genuss beim Essen.

```html
<!DOCTYPE html>
<html lang="de">
<head>
<meta charset="utf-8">
<title>1912 Zur Glutpfanne</title>
<link rel="stylesheet" href="https://fonts.googleapis.com/css2?family=Oswald:wght@500;700&family=Roboto+Condensed:wght@400&family=Lobster&family=Open+Sans:ital,wght@0,400;1,400&family=Arimo:ital,wght@0,400;0,700;1,700&family=Arvo:wght@700&family=Lora:ital@1&display=swap">
<style>
:root{
  --paper:#f7f6f4;
  --brown:#4a3a2e;
  --brown-dark:#3a2c22;
  --footer:#43362d;
  --clay:#a8715f;
  --coral:#f0594a;
  --star:#ef4b22;
  --mint:#7fcc9c;
  --ink:#1d1d1d;
  --muted:#777;
  --white:#fff;
}
*{margin:0;padding:0;box-sizing:border-box}
html,body{width:744px;height:1200px;overflow:hidden}
body{position:relative;background:var(--paper);font-family:"Open Sans",sans-serif;color:var(--ink)}
.abs{position:absolute}

/* header */
.nav-band{left:0;top:64px;width:744px;height:30px;background:var(--brown);border-top:3px solid var(--brown-dark);border-bottom:3px solid var(--brown-dark)}
.nav-band::after{content:"";position:absolute;left:0;right:0;top:3px;bottom:3px;border-top:1px solid #8a7462;border-bottom:1px solid #8a7462}
.nav-link{top:72px;font-family:"Oswald",sans-serif;font-weight:700;font-size:11px;letter-spacing:.5px;color:#f3e9dc;transform:translateX(-50%);white-space:nowrap}
.brand-badge{left:323px;top:28px;width:96px;height:96px;border-radius:50%;background:var(--brown);border:3px solid var(--white);box-shadow:0 0 0 2px var(--brown);display:flex;align-items:center;justify-content:center;text-align:center;z-index:3}
.brand-name{font-family:"Oswald",sans-serif;font-weight:700;font-size:15px;line-height:1.1;color:var(--white)}

/* hero */
.hero{left:0;top:99px;width:744px;height:300px;background:
  radial-gradient(ellipse 120px 70px at 500px 140px,rgba(214,48,28,.95),rgba(214,48,28,0) 100%),
  radial-gradient(ellipse 150px 60px at 470px 200px,rgba(246,196,92,.85),rgba(246,196,92,0) 100%),
  radial-gradient(ellipse 130px 55px at 540px 60px,rgba(176,106,50,.9),rgba(176,106,50,0) 100%),
  radial-gradient(ellipse 150px 45px at 520px 270px,rgba(92,50,30,.95),rgba(92,50,30,0) 100%),
  radial-gradient(ellipse 120px 70px at 230px 245px,rgba(236,176,84,.95),rgba(236,176,84,0) 100%),
  radial-gradient(ellipse 90px 80px at 70px 200px,rgba(196,150,110,.8),rgba(196,150,110,0) 100%),
  radial-gradient(ellipse 170px 60px at 200px 40px,rgba(110,62,36,.95),rgba(110,62,36,0) 100%),
  radial-gradient(ellipse 80px 40px at 300px 130px,rgba(128,164,52,.7),rgba(128,164,52,0) 100%),
  radial-gradient(ellipse 90px 50px at 700px 180px,rgba(120,160,50,.6),rgba(120,160,50,0) 100%),
  linear-gradient(180deg,#5a3a26 0%,#4a2f1f 60%,#3a2618 100%)}
.hero-arrow{top:207px;width:53px;height:53px}

/* section title ribbon */
.ribbon{left:259px;top:424px;width:264px;height:52px}
.ribbon-title{left:285px;top:426px;width:213px;height:39px;display:flex;align-items:center;justify-content:center;font-family:"Roboto Condensed",sans-serif;font-size:14px;letter-spacing:.4px;color:var(--white)}

/* cards */
.card{top:498px;width:181px;height:285px;background:var(--white);border:1px solid #b9b0a8;box-shadow:0 2px 4px rgba(0,0,0,.2)}
.card-photo{position:absolute;left:3px;top:3px;width:174px;height:137px}
.photo-bite{background:
  radial-gradient(ellipse 45px 25px at 86px 108px,rgba(200,110,40,.95),rgba(200,110,40,0) 100%),
  radial-gradient(ellipse 55px 40px at 86px 60px,rgba(226,182,150,.9),rgba(226,182,150,0) 100%),
  radial-gradient(ellipse 40px 30px at 86px 25px,rgba(120,80,50,.7),rgba(120,80,50,0) 100%),
  linear-gradient(180deg,#e2d2b4 0%,#d6c3a2 60%,#ece8e2 100%)}
.photo-grill{background:
  radial-gradient(ellipse 50px 20px at 60px 40px,rgba(110,80,70,.95),rgba(110,80,70,0) 100%),
  radial-gradient(ellipse 50px 20px at 130px 80px,rgba(110,80,70,.95),rgba(110,80,70,0) 100%),
  radial-gradient(ellipse 60px 25px at 110px 130px,rgba(240,130,30,.95),rgba(240,130,30,0) 100%),
  radial-gradient(ellipse 40px 25px at 20px 120px,rgba(230,110,20,.8),rgba(230,110,20,0) 100%),
  linear-gradient(180deg,#3c4c66 0%,#2f2a2c 50%,#5a2e16 100%)}
.photo-fries{background:
  radial-gradient(ellipse 70px 35px at 75px 80px,rgba(240,186,70,.98),rgba(240,186,70,0) 100%),
  radial-gradient(ellipse 35px 30px at 140px 80px,rgba(150,40,24,.9),rgba(150,40,24,0) 100%),
  radial-gradient(ellipse 18px 60px at 165px 30px,rgba(190,40,40,.7),rgba(190,40,40,0) 100%),
  linear-gradient(180deg,#8c8f92 0%,#b0b2b2 35%,#dcd6cc 85%,#f2efea 100%)}
.card-title{position:absolute;left:0;width:100%;top:149px;text-align:center;font-family:"Lobster",cursive;font-size:13px;color:#3a332e;letter-spacing:.3px}
.card-text{position:absolute;left:12px;right:10px;top:188px;font-style:italic;font-size:7.5px;line-height:1.45;color:var(--muted);letter-spacing:.2px}
.card-stars{position:absolute;left:12px;top:214px;font-size:14px;letter-spacing:1px;color:var(--star)}
.card-price{position:absolute;left:12px;top:242px;font-family:"Arimo",sans-serif;font-size:24px;color:var(--ink)}
.card-btn{position:absolute;left:95px;top:243px;width:69px;height:23px;background:var(--mint);border:2px solid var(--white);outline:1px solid var(--mint);color:var(--white);font-family:"Arimo",sans-serif;font-size:8.5px;display:flex;align-items:center;justify-content:center}

/* promo strip */
.promo{left:68px;top:840px;width:606px;height:151px;background:var(--clay)}
.promo::before,.promo::after{content:"";position:absolute;left:0;right:0;height:4px;background:radial-gradient(circle at 3px 0,var(--paper) 2px,transparent 2.5px) 0 0/6px 4px repeat-x}
.promo::before{top:0}
.promo::after{bottom:0;transform:rotate(180deg)}
.newsletter{left:84px;top:855px;width:158px;height:122px;background:var(--coral);border:3px solid var(--white)}
.newsletter-title{position:absolute;left:0;right:0;top:9px;text-align:center;font-family:"Arvo",serif;font-size:10.5px;color:var(--white);letter-spacing:.3px}
.newsletter-sub{position:absolute;left:0;right:0;top:23px;text-align:center;font-family:"Lora",serif;font-style:italic;font-size:8px;color:var(--white)}
.field{position:absolute;left:16px;width:120px;height:19px;background:var(--white);font-family:"Arimo",sans-serif;font-size:7px;color:#333;padding:6px 0 0 8px}
.go-btn{position:absolute;left:107px;top:93px;width:29px;height:14px;border:2px solid var(--white);border-radius:8px;font-family:"Arimo",sans-serif;font-weight:700;font-size:8px;color:var(--white);display:flex;align-items:center;justify-content:center}
.testi-title{left:295px;top:863px;font-family:"Arimo",sans-serif;font-weight:700;font-style:italic;font-size:11px;color:var(--white);letter-spacing:.4px}
.testi-text{left:295px;top:887px;width:160px;font-style:italic;font-size:7.8px;line-height:1.42;color:var(--white);white-space:nowrap}
.testi-name{left:295px;top:954px;font-style:italic;font-size:7.5px;color:var(--white)}
.testi-next{left:410px;top:955px;width:24px;height:18px;background:var(--white)}
.dish-title{left:475px;top:864px;font-family:"Arimo",sans-serif;font-weight:700;font-size:10px;color:var(--white)}
.dish-card{top:890px;width:86px;height:83px;border:2px solid var(--white)}
.dish-light{background:
  radial-gradient(ellipse 30px 18px at 42px 18px,rgba(200,150,130,.6),rgba(200,150,130,0) 100%),
  linear-gradient(180deg,#a57463 0%,#96695a 55%,#8c6152 100%)}
.dish-dark{background:
  radial-gradient(ellipse 30px 18px at 42px 18px,rgba(190,190,190,.5),rgba(190,190,190,0) 100%),
  radial-gradient(ellipse 40px 25px at 42px 60px,rgba(90,90,90,.7),rgba(90,90,90,0) 100%),
  linear-gradient(180deg,#3a3a3a 0%,#2a2a2a 100%)}

/* footer */
.footer{left:0;top:1016px;width:744px;height:184px;background:var(--footer)}
.foot-badge{left:24px;top:1044px;width:69px;height:69px;border-radius:50%;background:var(--brown-dark);border:2px solid var(--white);display:flex;align-items:center;justify-content:center;text-align:center}
.foot-badge .brand-name{font-size:11px}
.foot-heading{font-family:"Arimo",sans-serif;font-weight:700;font-size:8.5px;color:var(--white);letter-spacing:.3px}
.search{left:200px;top:1088px;width:186px;height:15px;background:var(--white);font-family:"Arimo",sans-serif;font-size:6px;color:#888;padding:4px 0 0 6px}
.social-head{left:446px;top:1036px;width:125px;height:27px;border-bottom:1px solid #7a6a5e}
.social-square{position:absolute;left:0;top:1px;width:21px;height:21px;background:#3b5b97}
.social-name{position:absolute;left:27px;top:10px;font-family:"Lobster",cursive;font-size:8.5px;color:var(--white)}
.social-stats{left:448px;top:1071px;font-family:"Arimo",sans-serif;font-weight:700;font-style:italic;font-size:5.6px;color:var(--white)}
.social-post{left:448px;top:1085px;width:135px;font-family:"Arimo",sans-serif;font-weight:700;font-style:italic;font-size:5.6px;line-height:1.3;color:var(--white);text-decoration:underline}
.mini-btn{top:1125px;height:7px;background:#4a67a8}
.mini-count{top:1125px;width:10px;height:7px;background:#eee}
.map{left:601px;top:1051px;width:112px;height:82px;border:2px solid var(--white);background:
  radial-gradient(ellipse 30px 20px at 20px 20px,rgba(170,200,225,.9),rgba(170,200,225,0) 100%),
  radial-gradient(ellipse 40px 25px at 75px 45px,rgba(226,222,200,.9),rgba(226,222,200,0) 100%),
  radial-gradient(ellipse 35px 20px at 40px 65px,rgba(196,214,170,.9),rgba(196,214,170,0) 100%),
  linear-gradient(135deg,#dfe2d2 0%,#d4ddc2 50%,#c8d6b6 100%)}
.foot-rule{left:25px;top:1150px;width:692px;height:1px;background:#6a5a4d}
.copyright{left:30px;top:1166px;font-family:"Arimo",sans-serif;font-size:8.5px;color:var(--white)}
.foot-link{top:1166px;font-family:"Arimo",sans-serif;font-size:8px;color:var(--white);transform:translateX(-50%)}
.foot-icon{top:1163px;width:20px;height:20px}
</style>
</head>
<body>

<!-- header -->
<div class="abs nav-band"></div>
<div class="abs nav-link" style="left:167px">Home</div>
<div class="abs nav-link" style="left:261px">Unser Restaurant</div>
<div class="abs nav-link" style="left:473px">Reservierungen</div>
<div class="abs nav-link" style="left:568px">Kontakt</div>
<div class="abs brand-badge"><span class="brand-name">1912<br>Zur<br>Glutpfanne</span></div>

<!-- hero slideshow -->
<div class="abs hero" role="img" aria-label="Foto: Burger mit Käse, Tomate und Zwiebelringen neben Pommes frites auf Holz"></div>
<svg class="abs hero-arrow" style="left:22px" viewBox="0 0 53 53" aria-label="Vorheriges Bild">
  <circle cx="26.5" cy="26.5" r="25" fill="none" stroke="#cfcac4" stroke-width="2"/>
  <path d="M38 26.5H16M25 17l-9 9.5 9 9.5" fill="none" stroke="#cfcac4" stroke-width="4"/>
</svg>
<svg class="abs hero-arrow" style="left:668px" viewBox="0 0 53 53" aria-label="Nächstes Bild">
  <circle cx="26.5" cy="26.5" r="25" fill="none" stroke="#cfcac4" stroke-width="2"/>
  <path d="M15 26.5h22M28 17l9 9.5-9 9.5" fill="none" stroke="#cfcac4" stroke-width="4"/>
</svg>

<!-- section title -->
<svg class="abs ribbon" viewBox="0 0 264 52">
  <polygon points="0,14 30,14 30,50 8,50 18,32" fill="#3d3028"/>
  <polygon points="264,14 234,14 234,50 256,50 246,32" fill="#3d3028"/>
  <polygon points="30,41 46,47 46,41" fill="#201812"/>
  <polygon points="234,41 218,47 218,41" fill="#201812"/>
  <rect x="26" y="2" width="213" height="39" fill="#4a3a2e"/>
  <rect x="29" y="5" width="207" height="33" fill="none" stroke="#fff" stroke-width="1.5"/>
</svg>
<div class="abs ribbon-title">Finden Sie die besten Burger</div>

<!-- cards -->
<article class="abs card" style="left:73px">
  <div class="card-photo photo-bite" role="img" aria-label="Foto: Kind beißt in einen großen Burger"></div>
  <h3 class="card-title">Neue Sorten</h3>
  <p class="card-text">“Lorem ipsum dolor sit amet, con-<br>sectetuer adipiscing elit,</p>
  <div class="card-stars">★★★★★</div>
  <div class="card-price">$9.99</div>
  <div class="card-btn">Read more</div>
</article>
<article class="abs card" style="left:282px">
  <div class="card-photo photo-grill" role="img" aria-label="Foto: Burger-Patties auf dem heißen Grillrost"></div>
  <h3 class="card-title">Höchster Rabatt</h3>
  <p class="card-text">“Lorem ipsum dolor sit amet, con-<br>sectetuer adipiscing elit,</p>
  <div class="card-stars">★★★★★</div>
  <div class="card-price">$9.99</div>
  <div class="card-btn">Read more</div>
</article>
<article class="abs card" style="left:487px">
  <div class="card-photo photo-fries" role="img" aria-label="Foto: Schale Pommes frites mit Currywurst"></div>
  <h3 class="card-title">Favoriten</h3>
  <p class="card-text">“Lorem ipsum dolor sit amet, con-<br>sectetuer adipiscing elit,</p>
  <div class="card-stars">★★★★★</div>
  <div class="card-price">$9.99</div>
  <div class="card-btn">Read more</div>
</article>

<!-- promo strip -->
<section class="abs promo"></section>
<form class="abs newsletter">
  <div class="newsletter-title">STAY UP-TO-DATE</div>
  <div class="newsletter-sub">join our newsletter</div>
  <div class="field" style="top:42px">Name</div>
  <div class="field" style="top:68px">Email Address</div>
  <div class="go-btn">GO</div>
</form>
<h4 class="abs testi-title">Testimonials:</h4>
<p class="abs testi-text">“Lorem ipsum dolor sit amet, con-<br>sectetuer adipiscing elit, sed diam<br>nonummy nibh euismod tincidunt ut<br>laoreet dolore magna aliquam erat<br>volutpat. ”</p>
<div class="abs testi-name">Beno Larwik</div>
<svg class="abs testi-next" viewBox="0 0 24 18" aria-label="Weiter">
  <rect width="24" height="18" fill="#fff"/>
  <path d="M6 9h11M14 6l3 3-3 3" fill="none" stroke="#333" stroke-width="1.2"/>
</svg>
<h4 class="abs dish-title">WÄHLEN SIE IHRE LISTE VON DISH</h4>
<div class="abs dish-card dish-light" style="left:476px" role="img" aria-label="Speisekarte auf Tafel, Vorschau mit Lupe"></div>
<div class="abs dish-card dish-dark" style="left:573px" role="img" aria-label="Speisekarte auf Tafel"></div>

<!-- footer -->
<footer class="abs footer"></footer>
<div class="abs foot-badge"><span class="brand-name">1912<br>Zur<br>Glutpfanne</span></div>
<div class="abs foot-heading" style="left:197px;top:1068px">FINDEN SIE UNS IN IHRER NÄHE</div>
<div class="abs search">Suchbereich</div>
<svg class="abs" style="left:368px;top:1090px" width="11" height="11" viewBox="0 0 11 11" aria-label="Suchen">
  <circle cx="4" cy="4" r="3" fill="none" stroke="#333" stroke-width="1.3"/>
  <path d="M6 6l4 4" stroke="#333" stroke-width="1.6"/>
</svg>
<div class="abs social-head"><span class="social-square"></span><span class="social-name">Zur Glutpfanne</span></div>
<div class="abs social-stats">651856 Fans · 3269 sprechen darüber</div>
<div class="abs social-post">Morgen ist es soweit. Die KNUSPERSTÄBE™ sind in deiner Stadt! Am 15. und 16. März kannst du eine kleine Portion gratis bei deinem Zur Glutpfanne</div>
<div class="abs mini-btn" style="left:448px;width:22px"></div>
<div class="abs mini-count" style="left:472px"></div>
<div class="abs mini-btn" style="left:487px;width:25px"></div>
<div class="abs mini-count" style="left:514px"></div>
<div class="abs foot-heading" style="left:593px;top:1034px">FINDEN SIE</div>
<div class="abs map" role="img" aria-label="Karte: Route durch Deutschland zum Restaurant"></div>
<div class="abs foot-rule"></div>
<div class="abs copyright">Copyright © 2014 All rights reserved.</div>
<div class="abs foot-link" style="left:277px">Home</div>
<div class="abs foot-link" style="left:362px">Unser Restaurant</div>
<div class="abs foot-link" style="left:445px">Reservierungen</div>
<div class="abs foot-link" style="left:522px">Kontakt</div>
<div class="abs foot-icon" style="left:631px;background:#3b5b97" aria-label="Soziales Netzwerk"></div>
<div class="abs foot-icon" style="left:663px;background:#1a72a8" aria-label="Soziales Netzwerk"></div>
<div class="abs foot-icon" style="left:693px;background:#d9463a" aria-label="Soziales Netzwerk"></div>

</body>
</html>
```